Clean bold and classy business card front and back
Kwr can be the logo
My name Trent Holloman as owner
Phone email and address
Owner Trent Holloman
Phone 8505550147
Email ridgelineinsulate@mailnest.example
Address170 frank pais rd Havana fl 32399

Industry/Entity Type

Business

Contact Information for Business Card

Owner Trent Holloman
Phone 8505550147

Requirements
Must have
• Keystone wall render under Kwr logo
Nice to have
• Bold and clean. Maybe use Kwr as logo and name under it. Have logo on one side and info on the other side with logo also
• Put a pic up. It doesn't have to be that but something that can be used
• Try some fancy fonts also

```html
<!DOCTYPE html>
<html lang="en">
<head>
<meta charset="utf-8">
<title>Kwr business card – front and back</title>
<link rel="stylesheet" href="https://fonts.googleapis.com/css2?family=Lexend:wght@400;600;800&family=Arimo&display=swap">
<style>
  :root {
    --sheet: #e0e0de;
    --label: #7a7a7a;
    --card-light: #ffffff;
    --card-dark: #0c0d0f;
    --brand-red: #f01c0a;
    --ink: #111111;
    --ink-soft: #f2f2f2;
    --mark-grey: #5b5b5b;
    --ghost-light: #f6f6f6;
    --ghost-dark: #131418;
  }
  * { margin: 0; padding: 0; box-sizing: border-box; }
  html, body { width: 902px; height: 1200px; overflow: hidden; }
  body {
    background: var(--sheet);
    position: relative;
    font-family: "Lexend", sans-serif;
  }
  .side-label {
    position: absolute;
    left: 85px;
    font-family: "Arimo", sans-serif;
    font-size: 27px;
    color: var(--label);
  }
  .side-label--front { top: 52px; }
  .side-label--back { top: 624px; }

  .card {
    position: absolute;
    left: 70px;
    width: 762px;
    overflow: hidden;
  }
  .card--front { top: 120px; height: 443px; background: var(--card-light); }
  .card--back { top: 680px; height: 442px; background: var(--card-dark); }

  .wordmark {
    position: absolute;
    font-weight: 800;
    line-height: 1;
    white-space: nowrap;
  }
  .ghost-mark {
    font-size: 300px;
    letter-spacing: 20px;
    transform: rotate(-14deg);
    transform-origin: left top;
  }
  .card--front .ghost-mark { color: var(--ghost-light); left: 40px; top: 150px; }
  .card--back .ghost-mark { color: var(--ghost-dark); left: 40px; top: 160px; }

  .front-brand { position: absolute; left: 55px; top: 80px; }
  .front-mark {
    position: static;
    font-size: 112px;
    letter-spacing: 6px;
    color: var(--brand-red);
  }
  .brand-line {
    font-weight: 600;
    text-transform: uppercase;
    white-space: nowrap;
  }
  .front-brand .brand-line {
    margin-top: 6px;
    padding-left: 4px;
    font-size: 15px;
    letter-spacing: 3.2px;
    color: var(--ink);
  }

  .holder { position: absolute; left: 47px; top: 258px; color: var(--ink); }
  .holder-name { font-size: 23px; font-weight: 600; letter-spacing: 0.5px; }
  .holder-role { font-size: 19px; font-weight: 600; margin-top: 8px; }

  .contact {
    position: absolute;
    right: 45px; top: 262px;
    text-align: right;
    color: var(--ink);
    font-weight: 600;
    font-size: 16px;
    letter-spacing: 0.5px;
  }
  .contact-address { margin-top: 14px; }

  .email-band {
    position: absolute;
    left: 0; top: 375px;
    width: 540px; height: 68px;
  }
  .email-band svg { position: absolute; inset: 0; }
  .email-text {
    position: absolute;
    left: 47px; top: 0;
    line-height: 68px;
    color: #fff;
    font-size: 14px;
    font-weight: 400;
    letter-spacing: 0.5px;
  }
  .band-mark {
    right: 10px; bottom: 2px;
    font-size: 66px;
    letter-spacing: 3px;
    color: var(--mark-grey);
  }

  .back-brand {
    position: absolute;
    left: 0; right: 0; top: 150px;
    text-align: center;
  }
  .back-mark {
    position: static;
    font-size: 150px;
    letter-spacing: 10px;
    color: var(--brand-red);
  }
  .back-brand .brand-line {
    margin-top: 10px;
    font-size: 20px;
    letter-spacing: 5px;
    color: var(--ink-soft);
  }
</style>
</head>
<body>
  <div class="side-label side-label--front">front</div>

  <section class="card card--front" aria-label="Card front">
    <div class="wordmark ghost-mark" aria-hidden="true">KWR</div>

    <div class="front-brand">
      <div class="wordmark front-mark">KWR</div>
      <div class="brand-line">Keystone wall render</div>
    </div>

    <div class="holder">
      <div class="holder-name">Trent Holloman</div>
      <div class="holder-role">Owner</div>
    </div>

    <div class="contact">
      <div class="contact-phone">8505550147</div>
      <div class="contact-address">428 dunmore ct Havana fl 32399</div>
    </div>

    <div class="email-band">
      <svg width="540" height="68" viewBox="0 0 540 68" aria-hidden="true">
        <polygon points="0,0 540,0 520,22 530,22 505,68 0,68" fill="var(--brand-red)"/>
      </svg>
      <div class="email-text">ridgelineinsulate@mailnest.example</div>
    </div>

    <div class="wordmark band-mark">KWR</div>
  </section>

  <div class="side-label side-label--back">back</div>

  <section class="card card--back" aria-label="Card back">
    <div class="wordmark ghost-mark" aria-hidden="true">KWR</div>
    <div class="back-brand">
      <div class="wordmark back-mark">KWR</div>
      <div class="brand-line">Keystone wall render</div>
    </div>
  </section>
</body>
</html>
```